Colour box Cat Fountain

We have designed the product logo, now want to move on for the product packaging box.

Using the new product logo.
Want to show a lovely housewife with lovely cat, not a big product photo.
See uploaded document for more details

Target Market(s)

USA, Germany, France

Industry/Entity Type

Product

Requirements
Must have
• a photo with lovely housewife with lovely cat

```html
<!DOCTYPE html>
<html lang="en">
<head>
<meta charset="utf-8">
<title>PurrSpring Cat Fountain – Box Panels</title>
<link href="https://fonts.googleapis.com/css2?family=Open+Sans:wght@400;600;700&family=Roboto+Condensed:wght@500;700&display=swap" rel="stylesheet">
<style>
  :root{
    --page:#f4f4f4;
    --panel:#ffffff;
    --band:#5b93c4;
    --band-text:#ffffff;
    --brand:#2f7fc1;
    --muted:#555555;
    --tile:#8c8c8c;
    --photo-a:#d9dde0;
    --photo-b:#b9a79c;
    --product-a:#8db9dc;
    --product-b:#c3c6c9;
  }
  *{box-sizing:border-box;margin:0;padding:0}
  html,body{width:1200px;height:998px;overflow:hidden;background:var(--page)}
  body{position:relative;font-family:"Open Sans",sans-serif}
  .panel{position:absolute;background:var(--panel);overflow:hidden;box-shadow:0 2px 10px rgba(0,0,0,.08)}
  .lid{left:370px;top:50px;width:600px;height:230px}
  .side{left:60px;top:300px;width:290px;height:620px}
  .front{left:370px;top:300px;width:600px;height:620px}

  /* shared brand lockup */
  .brand{display:flex;align-items:center;gap:8px;white-space:nowrap}
  .brand-name{font-family:"Open Sans",sans-serif;font-weight:600;color:var(--brand)}
  .brand-dot{border-radius:50%;background:var(--brand)}
  .brand-tag{font-size:8px;color:var(--muted);white-space:nowrap}

  /* lid panel */
  .lid .lockup{position:absolute;left:50%;top:62px;transform:translateX(-50%) rotate(180deg);display:flex;flex-direction:column;align-items:center;gap:2px}
  .lid .brand-name{font-size:26px;line-height:1}
  .lid .brand-dot{width:18px;height:18px}

  /* side panel */
  .side .product-photo{position:absolute;left:0;top:90px;width:100px;height:160px;border-radius:0 50px 50px 0;background:linear-gradient(160deg,var(--product-a),var(--product-b))}
  .side .band{position:absolute;left:80px;top:230px;width:210px;height:370px;background:var(--band);color:var(--band-text);padding:16px 12px 12px 14px;font-size:8.2px;line-height:1.4}
  .side .band p{margin-bottom:9px}
  .side .band ul{list-style:none}
  .side .band li::before{content:"• "}
  .side .lockup{position:absolute;left:16px;top:596px;transform:rotate(-90deg);transform-origin:0 0;display:flex;flex-direction:column;gap:0}
  .side .brand-name{font-size:32px;line-height:1.15}
  .side .brand-dot{width:22px;height:22px}
  .side .brand-tag{padding-left:30px}

  /* front panel */
  .front .hero-photo{position:absolute;left:270px;top:50px;width:240px;height:200px;background:radial-gradient(circle at 60% 40%,var(--photo-b),var(--photo-a) 70%)}
  .front .band{position:absolute;left:0;top:240px;width:510px;height:355px;background:var(--band);color:var(--band-text);padding:26px 30px 16px 36px}
  .title{font-family:"Roboto Condensed",sans-serif;font-weight:700;font-size:40px;line-height:1.1;letter-spacing:.5px;margin-bottom:12px}
  .intro{font-size:11px;line-height:1.38;margin-bottom:10px}
  .intro strong{font-weight:700}
  .features{list-style:none;font-size:11px;line-height:1.38}
  .features li{margin-bottom:7px}
  .features b{font-weight:700}
  .thumbs{position:absolute;left:522px;top:200px;width:80px;display:flex;flex-direction:column;gap:10px}
  .thumb{height:112px;border-radius:10px 0 0 10px;background:var(--tile);padding:8px 0 8px 8px}
  .thumb span{display:block;width:100%;height:100%;border-radius:6px 0 0 6px}
  .thumb.bowl span{background:linear-gradient(180deg,var(--product-a),#e8e2b0)}
  .thumb.filter span{background:linear-gradient(180deg,#3a3a3a,#6a6a6a)}
  .thumb.detail span{background:linear-gradient(180deg,#e7eef5,var(--product-a))}
</style>
</head>
<body>
  <section class="panel lid">
    <div class="lockup">
      <div class="brand"><span class="brand-dot"></span><span class="brand-name">PurrSpring</span></div>
      <span class="brand-tag">Fresh &amp; Filtered Water for Healthier Cats</span>
    </div>
  </section>

  <section class="panel side">
    <div class="product-photo" role="img" aria-label="Blue and grey cat water fountain product photo"></div>
    <div class="band">
      <p>BB manufactures more than 1 million water pumps and know how important it is for clean water. Fresh &amp; Filtered water encourages your cat to drink more water. <b>PurrSpring</b> is specially designed by BB &amp; KL Studio (a UK design consultant) together. It comes with multiple drinking level, surface skimmer, high quality water pump and easy change filter pad.</p>
      <p>All cats need a Cat Fountain, they instinctively prefer running water. More oxygen in running water and is more appealing to cats. <b>PurrSpring</b>'s filter pad includes sponge and activated carbon ensure better water quality all the time.</p>
      <p>PurrSpring can help to increase your cat's water intake to:</p>
      <ul>
        <li>Prevents UTI &amp; urinary disease</li>
        <li>Promotes healthy kidney function, including elimination of toxins and waste products</li>
        <li>Speeds recovery time for sick or injured pets</li>
        <li>Helps the body with energy conversion, temperature regulation, and fat metabolism</li>
      </ul>
    </div>
    <div class="lockup">
      <div class="brand"><span class="brand-dot"></span><span class="brand-name">PurrSpring</span></div>
      <span class="brand-tag">Fresh &amp; Filtered Water for Healthier Cats</span>
    </div>
  </section>

  <section class="panel front">
    <div class="hero-photo" role="img" aria-label="Smiling red-haired woman holding a grey cat"></div>
    <div class="band">
      <h1 class="title">CAT FOUNTAIN</h1>
      <p class="intro"><strong>Fresh &amp; Filtered</strong> water encourage your cat to drink more water leading to a healthier &amp; happier cat. (Water helps flushes out toxins, getting rid of waste through urination)</p>
      <ol class="features">
        <li><b>1)</b> Multiple drinking water level for cats of all sizes &amp; age</li>
        <li><b>2)</b> Surface skimmer aerates water &amp; ensures water surface remains crystal clear all the time</li>
        <li><b>3)</b> 3 months of worth of filter pads, each includes sponge &amp; activated carbon</li>
        <li><b>4)</b> Quiet &amp; low voltage water pump, backed by a 3 years Limited Warranty by BB Aquatics</li>
        <li><b>5)</b> Dishwasher friendly, easy to take apart without tools</li>
        <li><b>6)</b> Safe to use. Food grade Polypropylene, BPA free, Lead free, Phthalate free plastic bowl.</li>
      </ol>
    </div>
    <div class="thumbs">
      <div class="thumb bowl" role="img" aria-label="Fountain bowl and base parts"><span></span></div>
      <div class="thumb filter" role="img" aria-label="Replacement filter pads"><span></span></div>
      <div class="thumb detail" role="img" aria-label="Close-up of fountain water spout"><span></span></div>
    </div>
  </section>
</body>
</html>
```